Corvalent Growth Partners in need of a business card design

We need an innovative business card designed for a new company in Alberta, Canada. We assist organizations in improving performance by providing coaching and mentorship on how to promote and achieve organizational excellence. We teach senior leaders and their staff on how to continually improve performance; assist them in making sure the organization is innovative, competitive, and customer focused; support them in making sure the culture of the organization is also healthy, inclusive, and sustainable; and they are economically, socially, and environmentally responsible. We will do this by staying true to our company values of respect, excellence, integrity and trust.

Attached is our newly designed logo.

The team thought that having an inspirational quote similar to this one below would be a good addition somewhere on the card.

"Autograph your work with excellence.''

Target Market(s)

Private and public sector organizations. Once that are interested in being a Top 100 employer.

Industry/Entity Type

Business

Font styles to use
Sans Serif

Requirements
Must have
• 1. The business card must be double-sided.
2. Person's name and title
3. Email address
4. Phone number
5. Website (corvalentgrowth.ca)
6. QR code
7. A quote somewhere on the front of the card: Autograph your work with excellence.
Nice to have

```html
<!DOCTYPE html>
<html lang="en">
<head>
<meta charset="utf-8">
<title>Corvalent Growth Partners – Business Card</title>
<link rel="stylesheet" href="https://fonts.googleapis.com/css2?family=Open+Sans:wght@400;600;800&display=swap">
<style>
  :root {
    --bg: #e4e6e5;
    --paper: #ffffff;
    --ink: #2b2b2b;
    --muted: #6d6d6d;
    --faint: #b9b9b9;
    --purple: #7b5ea7;
    --green: #9dcb3c;
    --blue: #4b9fd6;
    --rule: #cfcfcf;
    --code-fill: #d9d9d9;
  }
  * { box-sizing: border-box; margin: 0; padding: 0; }
  html, body {
    width: 1200px; height: 900px; overflow: hidden;
    background: var(--bg);
    font-family: "Open Sans", Arial, sans-serif;
    color: var(--ink);
  }
  .sheet {
    width: 1200px; height: 900px;
    display: flex; flex-direction: column;
    align-items: center; justify-content: center; gap: 60px;
  }
  .card {
    position: relative;
    width: 560px; height: 320px;
    background: var(--paper);
    box-shadow: 0 6px 18px rgba(0,0,0,.12);
    overflow: hidden;
  }
  .stripe { position: absolute; display: flex; height: 20px; }
  .stripe span { display: block; height: 100%; }
  .stripe .purple { background: var(--purple); }
  .stripe .green { background: var(--green); }
  .stripe .blue { background: var(--blue); }

  /* quote side */
  .card--quote .stripe { left: 0; right: 0; bottom: 0; }
  .card--quote .purple { flex: 0 0 68%; }
  .card--quote .green { flex: 0 0 18%; }
  .card--quote .blue { flex: 1; }
  .wordmark {
    display: flex; align-items: center; gap: 10px;
    font-weight: 600; color: var(--ink); letter-spacing: -0.2px;
  }
  .wordmark .dot { width: 16px; height: 16px; border-radius: 50%; background: var(--green); flex: none; }
  .card--quote .wordmark { position: absolute; top: 78px; left: 0; right: 0; justify-content: center; font-size: 28px; }
  .quote {
    position: absolute; top: 160px; left: 70px; right: 70px;
    text-align: center; font-size: 13px; line-height: 1.55; color: var(--ink);
  }
  .quote cite { display: block; font-style: normal; color: var(--faint); margin-top: 2px; }

  /* contact side */
  .card--contact .stripe { top: 0; left: 300px; right: 0; }
  .card--contact .purple { flex: 0 0 56%; }
  .card--contact .green { flex: 0 0 22%; }
  .card--contact .blue { flex: 1; }
  .card--contact .wordmark {
    position: absolute; left: 36px; top: 160px; width: 220px;
    font-size: 20px; line-height: 1.2; align-items: center;
  }
  .card--contact .wordmark .name-text { display: block; }
  .divider { position: absolute; left: 282px; top: 60px; width: 1px; height: 170px; background: var(--rule); }
  .contact { position: absolute; left: 302px; top: 70px; }
  .contact .name { font-weight: 800; font-size: 19px; letter-spacing: .5px; line-height: 1; }
  .contact .title { font-size: 13px; color: var(--muted); margin-top: 2px; }
  .contact ul { list-style: none; margin-top: 16px; font-size: 13px; line-height: 2.3; }
  .qr-code {
    position: absolute; right: 28px; bottom: 26px;
    width: 62px; height: 62px; background: var(--code-fill);
  }
</style>
</head>
<body>
<main class="sheet">
  <section class="card card--quote" aria-label="Card front">
    <div class="wordmark"><span class="dot"></span>Corvalent Growth Partners</div>
    <p class="quote">“Every job is a self-portrait of the person who did it. Autograph your work with excellence.”
      <cite>Anonymous</cite></p>
    <div class="stripe"><span class="purple"></span><span class="green"></span><span class="blue"></span></div>
  </section>

  <section class="card card--contact" aria-label="Card back">
    <div class="stripe"><span class="purple"></span><span class="green"></span><span class="blue"></span></div>
    <div class="wordmark"><span class="dot"></span><span class="name-text">Corvalent Growth<br>Partners</span></div>
    <div class="divider"></div>
    <div class="contact">
      <p class="name">NAME</p>
      <p class="title">Title</p>
      <ul>
        <li>+123 456 789</li>
        <li>email@corvalentgrowth.ca</li>
        <li>www.corvalentgrowth.ca</li>
      </ul>
    </div>
    <div class="qr-code" role="img" aria-label="QR code linking to corvalentgrowth.ca"></div>
  </section>
</main>
</body>
</html>
```